Heronby Mortgage Capital Business Card

We need a business card design for our mortgage servicing company. In addition to servicing the loans of homeowners, we help homeowners with purchasing their homes and any mortgage refinancing. We would like to see designs that use the colors in the logo attached below (gold-ish yellow and navy blue), and any other design you deem fit! The design should communicate a simpler life with smart mortgages provided by Heronby.

```html
<!DOCTYPE html>
<html lang="en">
<head>
<meta charset="utf-8">
<title>Heronby Mortgage Capital – Business Card</title>
<link href="https://fonts.googleapis.com/css2?family=Montserrat:wght@400;500;700&display=swap" rel="stylesheet">
<style>
  :root {
    --navy-deep: #221e52;
    --navy-soft: #6a6590;
    --gold: #d9ad45;
    --paper: #f0f0f0;
    --ink-grey: #6e6e6e;
    --backdrop: #d4d4d4;
  }
  * { box-sizing: border-box; margin: 0; padding: 0; }
  html, body {
    width: 1200px; height: 1200px; overflow: hidden;
    background: var(--backdrop);
    font-family: "Montserrat", sans-serif;
  }
  .sheet {
    position: relative; width: 1200px; height: 1200px;
  }
  .card {
    position: absolute; left: 160px; width: 880px; height: 503px;
    border-radius: 26px;
    box-shadow: 0 10px 30px rgba(0,0,0,0.18);
    overflow: hidden;
  }
  .card--front {
    top: 70px;
    background: linear-gradient(100deg, var(--navy-soft) 0%, #4c4676 35%, var(--navy-deep) 75%);
    display: flex; align-items: center; justify-content: center;
  }
  .card--back {
    top: 627px;
    background: var(--paper);
  }
  .brand {
    display: flex; align-items: center; gap: 18px;
    color: var(--gold); font-weight: 700;
  }
  .brand__dot {
    width: 22px; height: 22px; border-radius: 50%; background: var(--gold);
  }
  .brand--large { font-size: 64px; }
  .brand--small {
    position: absolute; top: 70px; right: 70px;
    font-size: 36px; gap: 12px;
  }
  .brand--small .brand__dot { width: 14px; height: 14px; }
  .person {
    position: absolute; left: 70px; bottom: 60px;
  }
  .person__name {
    color: var(--gold); font-weight: 700; font-size: 38px; letter-spacing: 0.5px;
  }
  .person__role {
    color: var(--ink-grey); font-size: 22px; margin: 8px 0 14px 14px;
  }
  .contact { list-style: none; margin-left: 14px; }
  .contact__item {
    display: flex; align-items: center; gap: 16px;
    color: var(--ink-grey); font-size: 22px; line-height: 36px;
  }
  .contact__icon { width: 20px; height: 20px; fill: var(--gold); flex: none; }
  .address {
    position: absolute; right: 70px; bottom: 150px;
    text-align: right; color: var(--ink-grey); font-size: 22px; line-height: 32px;
  }
</style>
</head>
<body>
<main class="sheet">
  <section class="card card--front" aria-label="Card front">
    <div class="brand brand--large">
      <span class="brand__dot"></span>
      <span class="brand__name">Heronby Mortgage</span>
    </div>
  </section>

  <section class="card card--back" aria-label="Card back">
    <div class="brand brand--small">
      <span class="brand__dot"></span>
      <span class="brand__name">Heronby Mortgage</span>
    </div>

    <div class="person">
      <h1 class="person__name">Dorian Vale</h1>
      <p class="person__role">Founder &amp; Director</p>
      <ul class="contact">
        <li class="contact__item">
          <svg class="contact__icon" viewBox="0 0 24 24" aria-hidden="true"><path d="M6.6 10.8a15.1 15.1 0 0 0 6.6 6.6l2.2-2.2a1 1 0 0 1 1-.25 11.4 11.4 0 0 0 3.6.57 1 1 0 0 1 1 1V20a1 1 0 0 1-1 1A17 17 0 0 1 3 4a1 1 0 0 1 1-1h3.5a1 1 0 0 1 1 1c0 1.25.2 2.45.57 3.6a1 1 0 0 1-.25 1z"/></svg>
          (555)-010-4821
        </li>
        <li class="contact__item">
          <svg class="contact__icon" viewBox="0 0 24 24" aria-hidden="true"><path d="M2 5h20v14H2z M2 5l10 8 10-8" /></svg>
          info@heronbymtg.com
        </li>
        <li class="contact__item">
          <svg class="contact__icon" viewBox="0 0 24 24" aria-hidden="true"><path d="M12 2a10 10 0 1 0 0 20 10 10 0 0 0 0-20zm6.9 9h-3a15 15 0 0 0-1.3-5.6A8 8 0 0 1 18.9 11zM12 4.1c.9 1.2 1.7 3.6 1.9 6.9h-3.8c.2-3.3 1-5.7 1.9-6.9zM9.4 5.4A15 15 0 0 0 8.1 11h-3a8 8 0 0 1 4.3-5.6zM5.1 13h3a15 15 0 0 0 1.3 5.6A8 8 0 0 1 5.1 13zm6.9 6.9c-.9-1.2-1.7-3.6-1.9-6.9h3.8c-.2 3.3-1 5.7-1.9 6.9zm2.6-1.3a15 15 0 0 0 1.3-5.6h3a8 8 0 0 1-4.3 5.6z"/></svg>
          www.heronbymtg.com
        </li>
      </ul>
    </div>

    <p class="address">218 Harbor Ln S, Bayview,<br>FL 34010</p>
  </section>
</main>
</body>
</html>
```